Crestline Slate & Tile Needs a Business Card

Attached you will find your logo, my photo and design guidelines for a new business card. The final design will need two separate files to create an embossed card. The cards will be printed by www.plinkprint.com (Instructions below)
Format is the Zib SQUARE card
Crestline Slate And Tile is a brick and mortar, retail stone and tile shop.
One the front:
Crestline Slate And Tile
Gerald Finchcombe
Owner
48207 Vesper Hollow Blvd
Suite R & T
Charlotte, NC 28953
Cell: 704-555-0183
Web: www.CrestlineSlateAndTile.com
(Make each word of the domain a different or alternating color)
On the back;
Something that shows beautiful colorful tile
Follow the design guide closely please. For more information see this page that describes creating the spot gloss file: https://www.plinkprint.com/us/business-cards/design-guidelines-spot-gloss
The logo is what we would like to have raised spot glossed.
Format is the Zib SQUARE card. See attahced guidlines.

```html
<!DOCTYPE html>
<html lang="en">
<head>
<meta charset="utf-8">
<title>Crestline Slate &amp; Tile — Square Business Card</title>
<link rel="stylesheet" href="https://fonts.googleapis.com/css2?family=Cinzel:wght@600&family=Libre+Baskerville:wght@700&family=Lato:wght@400;700&display=swap">
<style>
  :root {
    --stage: #0b0b0b;
    --paper: #faf8f4;
    --navy: #1d2a36;
    --gold: #b08234;
    --rust: #b8482a;
    --ink: #2a2a2a;
    --cobalt: #1d3a9a;
    --saffron: #f2a81c;
    --cream: #f3efe6;
    --photo-dark: #2f2f31;
  }
  * { box-sizing: border-box; margin: 0; padding: 0; }
  html, body { width: 1200px; height: 800px; overflow: hidden; background: var(--stage); }
  .canvas { position: relative; width: 1200px; height: 800px; }

  .card {
    position: absolute; top: 150px; width: 500px; height: 500px;
    border-radius: 34px; overflow: hidden;
  }
  .card--back { left: 70px; }
  .card--front { left: 630px; background: var(--paper); }

  .tile-artwork {
    width: 100%; height: 100%;
    background: radial-gradient(circle at 50% 50%, #e9772a 0%, var(--saffron) 14%, var(--cream) 38%, var(--saffron) 58%, var(--cobalt) 82%, #17307f 100%);
  }

  .brand { position: absolute; left: 36px; top: 40px; display: flex; align-items: center; gap: 16px; }
  .brand__mark { width: 70px; height: 70px; background: var(--navy); }
  .brand__name {
    font-family: "Cinzel", serif; font-weight: 600; color: var(--navy);
    font-size: 27px; letter-spacing: 3px; line-height: 1.15;
  }

  .portrait {
    position: absolute; right: 26px; top: 150px; width: 220px; height: 230px;
    border: 3px solid var(--gold);
    background: linear-gradient(160deg, #444447, var(--photo-dark) 55%, #2c3650);
  }

  .person { position: absolute; left: 24px; top: 192px; width: 220px; text-align: center; }
  .person__name {
    font-family: "Libre Baskerville", serif; font-weight: 700; color: var(--navy);
    font-size: 19px; line-height: 1.2; white-space: nowrap;
  }
  .person__role {
    display: flex; align-items: center; gap: 10px; justify-content: center; margin-top: 8px;
    font-family: "Lato", sans-serif; font-weight: 700; color: var(--rust);
    font-size: 12px; letter-spacing: 5px;
  }
  .person__role::before, .person__role::after { content: ""; width: 34px; height: 1px; background: var(--gold); }

  .contact {
    position: absolute; left: 32px; top: 270px; width: 210px; list-style: none;
    font-family: "Lato", sans-serif; color: var(--ink); font-size: 11.5px;
  }
  .contact__item { display: flex; align-items: flex-start; gap: 8px; margin-bottom: 9px; line-height: 1.35; white-space: nowrap; }
  .contact__icon { width: 13px; height: 13px; flex: none; margin-top: 1px; }
  .domain-a { color: var(--navy); }
  .domain-b { color: var(--rust); }

  .values-rule { position: absolute; left: 0; right: 0; bottom: 64px; height: 2px; background: var(--gold); }
  .values-rule__gem {
    position: absolute; left: 50%; top: -5px; width: 10px; height: 10px;
    background: var(--gold); transform: translateX(-50%) rotate(45deg);
  }
  .values {
    position: absolute; left: 0; right: 0; bottom: 0; height: 62px; background: var(--navy);
    display: flex; align-items: center; justify-content: center; gap: 14px;
    font-family: "Lato", sans-serif; font-weight: 700; color: #fff;
    font-size: 12px; letter-spacing: 5px;
  }
  .values__dot { color: var(--rust); letter-spacing: 0; }
</style>
</head>
<body>
<main class="canvas">

  <section class="card card--back">
    <div class="tile-artwork" role="img" aria-label="Hand-painted majolica tile with a central orange and blue flower, cream medallion, green leaves and saffron scrolls on cobalt blue"></div>
  </section>

  <section class="card card--front">
    <div class="brand">
      <span class="brand__mark"></span>
      <span class="brand__name">Crestline<br>Slate &amp; Tile</span>
    </div>

    <div class="portrait" role="img" aria-label="Portrait photo of the owner in a checked navy blazer against a dark grey studio backdrop"></div>

    <div class="person">
      <h1 class="person__name">Gerald Finchcombe</h1>
      <p class="person__role">OWNER</p>
    </div>

    <ul class="contact">
      <li class="contact__item">
        <svg class="contact__icon" viewBox="0 0 24 24"><path fill="#b8482a" d="M6.6 10.8a15 15 0 0 0 6.6 6.6l2.2-2.2a1 1 0 0 1 1-.25 11.4 11.4 0 0 0 3.6.57 1 1 0 0 1 1 1V20a1 1 0 0 1-1 1A17 17 0 0 1 3 4a1 1 0 0 1 1-1h3.5a1 1 0 0 1 1 1c0 1.25.2 2.45.57 3.570a1 1 0 0 1-.25 1z"/></svg>
        <span>704-555-0183</span>
      </li>
      <li class="contact__item">
        <svg class="contact__icon" viewBox="0 0 24 24"><path fill="#b8482a" d="M2 5h20v14H2z"/><path fill="none" stroke="#faf8f4" stroke-width="1.8" d="M2 5l10 8 10-8"/></svg>
        <span>www.<span class="domain-a">Crestline</span><span class="domain-b">Slate</span><span class="domain-a">And</span><span class="domain-b">Tile</span>.com</span>
      </li>
      <li class="contact__item">
        <svg class="contact__icon" viewBox="0 0 24 24"><path fill="#b8482a" d="M12 2a7 7 0 0 0-7 7c0 5.2 7 13 7 13s7-7.8 7-13a7 7 0 0 0-7-7zm0 9.5A2.5 2.5 0 1 1 12 6.5a2.5 2.5 0 0 1 0 5z"/></svg>
        <span>48207 Vesper Hollow Blvd<br>Suite R &amp; T Charlotte,<br>NC 28953</span>
      </li>
    </ul>

    <div class="values-rule"><span class="values-rule__gem"></span></div>
    <footer class="values">
      <span>QUALITY</span><span class="values__dot">◆</span>
      <span>CRAFTSMANSHIP</span><span class="values__dot">◆</span>
      <span>INTEGRITY</span>
    </footer>
  </section>

</main>
</body>
</html>
```